Granite Tile Retail Website

We need wireframe PSD for a website selling granite tile. There are 4 custom pages, shopping cart page, and checkout page. I have a logo designed but the color scheme is up to you.
Color Gallery - We have approximately 20 different stone colors. Each color will have a little gallery of its own pictures. On this page the customer can also add a sample piece of the color they are viewing to their shopping cart.
Questions Page - This page has 3 elements
1. Upload or fax diagram of kitchen for quotation
2. Installation video
3. Installation FAQ (text)
Order Page - This page has 3 steps for the customer
1. Customer chooses his color.
2. For each color we have numerous different products. He inputs the quantity of each product.
3. Customer is given total price and shipping quote. If order over $500 it says "This order qualifies for free shipping". Customer can click on button to "Order Now"
Shopping Cart - Very standard, just like I have attached here. Just modify for your colors / font.
Checkout - Just like in the attached. See design-explanation.docx for minor adjustments.
I have vector file for logo.
Please try to post your designs by tonightÂ
Home owners 40-60 years old
Shopping

```html
<!DOCTYPE html>
<html lang="en">
<head>
<meta charset="utf-8">
<title>Ridgeway Granite – Color Gallery</title>
<link rel="stylesheet" href="https://fonts.googleapis.com/css2?family=Arimo:wght@400;700&family=Marcellus&display=swap">
<style>
:root{
  --teal:#4f8d88;
  --teal-dark:#3f7a75;
  --teal-deep:#2f5f5b;
  --orange:#f5b000;
  --orange-light:#ffc933;
  --orange-btn:#f2a81e;
  --ink:#222;
  --ink-soft:#444;
  --panel-line:#d9d9d9;
  --panel-bg:#f4f4f4;
  --footer-link:#e8f3f2;
  --preview:#3366ff;
}
*{margin:0;padding:0;box-sizing:border-box}
html,body{width:1200px;height:979px;overflow:hidden}
body{position:relative;background:#fff;font-family:"Arimo",Arial,sans-serif;color:var(--ink)}
.abs{position:absolute}

/* header */
.site-header{left:0;top:0;width:1200px;height:96px;background:linear-gradient(#5a9a95,var(--teal) 60%,var(--teal-dark))}
.brand{left:240px;top:14px;height:63px;display:flex;align-items:center;gap:10px}
.brand-mark{width:22px;height:22px;background:var(--orange)}
.brand-name{font:700 26px "Arimo",Arial,sans-serif;color:#fff;letter-spacing:1px}
.cart-status{left:869px;top:0;width:108px;height:27px;background:var(--teal-deep);border-radius:0 0 4px 4px;display:flex;align-items:center;gap:6px;padding-left:8px}
.cart-dot{width:16px;height:16px;border-radius:50%;background:#f2c14e}
.cart-status p{font-size:8px;line-height:10px;color:#dfeeed}
.cart-status b{color:var(--orange-light)}
.main-nav{left:490px;top:57px;height:30px;display:flex;align-items:center}
.main-nav a{font:700 12px "Arimo",Arial,sans-serif;color:#fff;text-decoration:none;text-transform:uppercase;padding:0 14px;height:30px;line-height:30px}
.main-nav a.is-active{background:linear-gradient(var(--orange-light),var(--orange));border-radius:4px;color:#fff;padding:0 16px;margin-right:12px;box-shadow:0 0 0 1px #d89a00}
.main-nav .gap{margin-right:14px}

/* title band */
.title-band{left:0;top:96px;width:1200px;height:128px;background:linear-gradient(#dcdcdc,#fff)}
.page-icon{left:225px;top:132px;width:37px;height:37px;border-radius:50%;background:conic-gradient(#e23b3b,#f5b000,#4bbf4b,#3366ff,#9b3bd6,#e23b3b)}
.page-title{left:271px;top:130px;font:400 31px "Marcellus",Georgia,serif;color:#1d1d1d}

/* palette */
.palette{left:223px;top:226px;width:259px;height:590px;background:linear-gradient(#fafafa,var(--panel-bg));border:2px solid var(--panel-line);border-radius:8px}
.swatch{position:absolute;width:62px;text-align:center}
.swatch i{display:block;width:62px;height:50px;border:1px solid #333}
.swatch span{display:block;font-size:9px;line-height:11px;color:var(--ink-soft);margin-top:3px;white-space:nowrap}

.preview{left:528px;top:226px;width:446px;height:285px;background:var(--preview);border-radius:6px;box-shadow:0 14px 10px -8px rgba(0,0,0,.18)}
.order-btn{left:831px;top:540px;width:141px;height:31px;background:linear-gradient(#f9c24a,var(--orange-btn));border-radius:3px;font:400 15px "Marcellus",Georgia,serif;color:#3a2a00;text-align:center;line-height:31px;box-shadow:0 8px 8px -6px rgba(0,0,0,.2)}

.chosen{position:absolute;width:87px;text-align:center}
.chosen i{display:block;width:87px;height:67px;border:1px solid #222}
.chosen span{display:block;font:700 13px/16px "Arimo",Arial,sans-serif;color:#222;margin-top:4px}
.chosen span+span{margin-top:0}

/* footer */
.footer-fade{left:0;top:823px;width:1200px;height:55px;background:linear-gradient(#fff,#d8d8d8)}
.site-footer{left:0;top:878px;width:1200px;height:101px;background:linear-gradient(var(--teal),var(--teal-dark))}
.footer-links{position:absolute;top:20px;list-style:none}
.footer-links li{font-size:10px;line-height:24px;color:var(--footer-link)}
.footer-links li::before{content:"→";margin-right:5px;font-size:8px}
.footer-brand{left:886px;top:19px;display:flex;align-items:center;gap:5px}
.footer-brand .brand-mark{width:10px;height:10px}
.footer-brand .brand-name{font-size:13px}
.copyright{right:221px;top:64px;text-align:right;font-size:10px;line-height:16px;color:#e4efee}
</style>
</head>
<body>

<header class="abs site-header">
  <div class="abs brand" style="left:240px"><span class="brand-mark"></span><span class="brand-name">RIDGEWAY</span></div>
  <div class="abs cart-status"><span class="cart-dot"></span><p>Now in your cart<br><b>0 items</b></p></div>
  <nav class="abs main-nav">
    <a class="is-active" href="#">Home</a>
    <a class="gap" href="#">Gallery</a>
    <a class="gap" href="#">Questions</a>
    <a class="gap" href="#">Orderr</a>
    <a href="#">Shopping Cart</a>
  </nav>
</header>

<div class="abs title-band"></div>
<div class="abs page-icon" role="img" aria-label="Colour palette icon"></div>
<h1 class="abs page-title">Color Gallery</h1>

<section class="abs palette" aria-label="Stone colours">
  <div class="swatch" style="left:18px;top:24px"><i style="background:#0a4cff"></i><span>51.102.255</span><span>#3366FF</span></div>
  <div class="swatch" style="left:99px;top:24px"><i style="background:#4a00ff"></i><span>102.51.255</span><span>#6633FF</span></div>
  <div class="swatch" style="left:176px;top:24px"><i style="background:#12ff4c"></i><span>51.255.102</span><span>#33FF66</span></div>

  <div class="swatch" style="left:18px;top:120px"><i style="background:#00c2ff"></i><span>51.204.255</span><span>#33CCFF</span></div>
  <div class="swatch" style="left:99px;top:120px"><i style="background:#0014ff"></i><span>0.61.245</span><span>#003DF5</span></div>
  <div class="swatch" style="left:176px;top:120px"><i style="background:#44ff00"></i><span>102.255.51</span><span>#66FF33</span></div>

  <div class="swatch" style="left:18px;top:214px"><i style="background:#00ffc4"></i><span>51.255.204</span><span>#33FFCC</span></div>
  <div class="swatch" style="left:99px;top:214px"><i style="background:#a86c00"></i><span>184.138.0</span><span>#B88A00</span></div>
  <div class="swatch" style="left:176px;top:214px"><i style="background:#c4ff00"></i><span>204.255.51</span><span>#CCFF33</span></div>

  <div class="swatch" style="left:18px;top:303px"><i style="background:#00109c"></i><span>0.46.184</span><span>#002EB8</span></div>
  <div class="swatch" style="left:99px;top:303px"><i style="background:#ff0a48"></i><span>255.51.102</span><span>#FF3366</span></div>
  <div class="swatch" style="left:176px;top:303px"><i style="background:#f5c000"></i><span>255.204.51</span><span>#FFCC33</span></div>

  <div class="swatch" style="left:18px;top:396px"><i style="background:#f5a800"></i><span>245.184.0</span><span>#F5B800</span></div>
  <div class="swatch" style="left:99px;top:396px"><i style="background:#ff4a08"></i><span>255.102.51</span><span>#FF6633</span></div>
  <div class="swatch" style="left:176px;top:396px"><i style="background:#a86c00"></i><span>184.138.0</span><span>#B88A00</span></div>

  <div class="swatch" style="left:18px;top:489px"><i style="background:#f5f500"></i><span>245.184.0</span><span>#F5B800</span></div>
  <div class="swatch" style="left:99px;top:489px"><i style="background:#ff8800"></i><span>255.102.51</span><span>#FF6633</span></div>
  <div class="swatch" style="left:176px;top:489px"><i style="background:#f5d800"></i><span>184.138.0</span><span>#B88A00</span></div>
</section>

<div class="abs preview" aria-label="Selected colour preview"></div>
<div class="abs order-btn">Make Full Order</div>

<section aria-label="Chosen colours">
  <div class="chosen" style="left:528px;top:603px"><i style="background:#0044ff"></i><span>51.102.255</span><span>#3366FF</span></div>
  <div class="chosen" style="left:648px;top:603px"><i style="background:#4400ff"></i><span>102.51.255</span><span>#6633FF</span></div>
  <div class="chosen" style="left:768px;top:603px"><i style="background:#b800ff"></i><span>204.51.255</span><span>#CC33FF</span></div>
  <div class="chosen" style="left:888px;top:603px"><i style="background:#ff00b8"></i><span>255.51.204</span><span>#FF33CC</span></div>
  <div class="chosen" style="left:528px;top:710px"><i style="background:#00c2ff"></i><span>51.204.255</span><span>#33CCFF</span></div>
  <div class="chosen" style="left:648px;top:710px"><i style="background:#0014ff"></i><span>0.61.245</span><span>#003DF5</span></div>
  <div class="chosen" style="left:768px;top:710px"><i style="background:#00109c"></i><span>0.46.184</span><span>#002EB8</span></div>
  <div class="chosen" style="left:888px;top:710px"><i style="background:#ff0a48"></i><span>255.51.102</span><span>#FF3366</span></div>
</section>

<div class="abs footer-fade"></div>
<footer class="abs site-footer">
  <ul class="footer-links" style="left:218px"><li>Home</li><li>Gallery</li><li>Questions</li></ul>
  <ul class="footer-links" style="left:331px"><li>Orderr</li><li>Shopping Cart</li><li>Contact Us</li></ul>
  <ul class="footer-links" style="left:468px"><li>Return Policy</li><li>Shipping Policy</li><li>Privacy</li></ul>
  <ul class="footer-links" style="left:597px"><li>Terms of Use</li><li>Customer Service</li></ul>
  <div class="abs footer-brand"><span class="brand-mark"></span><span class="brand-name">RIDGEWAY</span></div>
  <p class="abs copyright">© 2011 Ridgeway.com.<br>All Rights Reserved.</p>
</footer>

</body>
</html>
```